Maple Cove Laser Dermal Studio needs an 8 page WP redesign

We need a colorful re-design for an 8 page Wordpress website. The current preliminary website is live. The home page URL is http://maplecovelaserdermalstudio.com The new logo is live on the website also. I would like a (re)design using the colors that are represented by the new logo file, and any additional complimentary colors. The information regarding the business can be found on the website already, so please review it for insight. The name of the business is "Maple Cove Laser Dermal Studio".

Target Market(s)

The targeted website viewer is an adult female between the ages of 30 and 75 who is interested in facial renewal, wart removal and scar removal. This website should inspire in the target viewer the benefits of laser facial renewal, wart removal and new scar removal. Potential website viewers are wanting and searching for improved skin health and appearance. The website must represent the essence of a professional spa business.

Industry/Entity Type

Business

Font styles to use
Sans Serif

Requirements
Must have
• - The phone number placed in a visible and high value widget area that allows mobile phone browser dialing.

```html
<!DOCTYPE html>
<html lang="en">
<head>
<meta charset="utf-8">
<title>Maple Cove Laser Dermal Studio</title>
<link rel="stylesheet" href="https://fonts.googleapis.com/css2?family=Open+Sans:wght@400;600;700&family=Fjalla+One&family=Oswald:wght@500&family=Arimo:wght@400;700&display=swap">
<style>
:root{
  --purple:#9a5bbd;
  --purple-soft:#b37fcb;
  --purple-deep:#7b3b91;
  --plum:#573657;
  --plum-dark:#4a2c4a;
  --ink:#222;
  --ink-soft:#555;
  --muted:#888;
  --grey-bar:#f3f3f3;
  --grey-box:#ececec;
  --grey-section:#ebebeb;
  --white:#fff;
}
*{margin:0;padding:0;box-sizing:border-box}
html,body{width:683px;height:1200px;overflow:hidden;background:var(--white)}
body{position:relative;font-family:"Open Sans",Arial,sans-serif;color:var(--ink)}
.abs{position:absolute}
a{color:inherit;text-decoration:none}

/* top bar */
.top-bar{left:0;top:0;width:683px;height:24px;background:var(--grey-bar);border-bottom:1px solid #e2e2e2;font-size:8px}
.top-bar .item{position:absolute;top:7px;display:flex;align-items:center;gap:5px}
.top-bar .phone{left:409px;color:var(--ink)}
.top-bar .mail{left:493px;color:var(--purple)}

/* header */
.brand{left:38px;top:36px;display:flex;align-items:center;gap:7px}
.brand-dot{width:14px;height:14px;border-radius:50%;background:var(--purple)}
.brand-name{font-family:"Open Sans",sans-serif;font-weight:700;font-size:12px;line-height:14px;color:var(--plum)}
.main-nav{left:235px;top:68px;display:flex;font-size:7.5px;text-transform:uppercase;color:var(--ink-soft)}
.main-nav a{padding:5px 6px;height:19px;margin-right:2px}
.main-nav a.active{background:var(--purple);color:var(--white);border-radius:2px 2px 0 0}
.header-rule{left:0;top:93px;width:683px;border-top:2px dashed #cfcfcf}

/* hero */
.hero{left:0;top:97px;width:683px;height:280px;background:linear-gradient(90deg,#fafafa 0%,#fbf6f3 45%,#f4e1d3 100%);overflow:hidden}
.hero-photo{position:absolute;right:0;top:0;width:400px;height:280px;background:radial-gradient(ellipse at 70% 40%,#f3d2bc 0%,#efcab8 35%,#f1c7cf 60%,rgba(250,246,244,0) 85%)}
.hero-title{left:44px;top:170px;font-family:"Fjalla One",sans-serif;font-size:27px;color:#2e1f2e}
.hero-tagline{left:43px;top:204px;font-size:33px;color:var(--purple-soft);letter-spacing:.5px}
.hero-offer{left:43px;top:240px;font-size:19px;color:var(--purple-soft)}
.hero-offer strong{color:#2e1f2e;font-weight:600}
.hero-phone{left:44px;top:265px;font-size:21px;color:#111}
.slider-dots{left:308px;top:341px;display:flex;gap:9px}
.slider-dots span{width:15px;height:15px;border-radius:50%;background:#241623}
.slider-dots span.on{background:var(--purple)}

/* welcome band */
.welcome{left:0;top:378px;width:683px;height:130px;background:var(--purple-soft);border-top:3px solid var(--purple-deep);text-align:center;color:var(--white)}
.welcome h1{font-weight:400;font-size:19px;color:#1d1020;margin-top:14px}
.welcome p{font-size:8px;line-height:14.5px;width:600px;margin:13px auto 0}
.welcome mark{background:#2e1a33;color:var(--white);padding:0 1px}

/* FAQ */
.section-title{font-weight:400;font-size:19px;color:var(--ink)}
.faq-title{left:38px;top:530px}
.faq{left:38px;top:568px;width:295px}
.faq-item{background:var(--grey-box);margin-bottom:6px}
.faq-head{display:flex;align-items:center;height:23px;font-size:8.5px;color:var(--ink)}
.faq-toggle{width:22px;height:23px;background:var(--purple);color:var(--white);display:flex;align-items:center;justify-content:center;font-size:14px;margin-right:8px;line-height:1}
.faq-body{margin-left:22px;padding:6px 10px 12px 10px;background:#f2f2f2;font-size:7.3px;line-height:14px;color:var(--ink-soft);border-left:0}
.faq-item.open{border-left:22px solid #d8d8d8}
.faq-item.open .faq-head{margin-left:-22px}
.faq-item.open .faq-body{margin-left:0}
.faq-body p+p{margin-top:10px}

/* results */
.results-title{left:355px;top:530px}
.gallery-link{left:603px;top:538px;font-size:8px;color:var(--plum);text-decoration:underline;display:flex;align-items:center;gap:4px}
.results-text{left:355px;top:563px;width:290px;font-size:7.6px;line-height:14px;color:var(--ink)}
.shot{width:68px}
.shot .photo{height:60px}
.shot .label{height:16px;font-size:7.5px;display:flex;align-items:center;justify-content:center}
.shot.before .label{background:#d9d9d9;color:var(--ink)}
.shot.after .label{background:var(--plum);color:var(--white)}
.tone-a{background:linear-gradient(160deg,#c99a86,#a97462)}
.tone-b{background:linear-gradient(160deg,#e2b8a6,#c99482)}
.tone-c{background:linear-gradient(160deg,#d49a70,#b47a52)}
.tone-d{background:linear-gradient(160deg,#ecc4a8,#d6a58a)}
.tone-e{background:linear-gradient(160deg,#e8ada6,#d59489)}
.tone-f{background:linear-gradient(160deg,#f2cdbe,#e4b2a2)}
.tone-g{background:linear-gradient(160deg,#f0c9b8,#dea08e)}
.tone-h{background:linear-gradient(160deg,#f5d8c9,#e9bfae)}

/* call to action */
.cta{left:38px;top:827px;width:608px;height:95px;background:linear-gradient(90deg,#e9e9e9 0%,#f5f5f5 55%,#f7f7f7 100%);overflow:hidden}
.cta-photo{position:absolute;left:0;top:0;width:330px;height:95px;background:linear-gradient(90deg,#bdbdbd 0%,#cfcfcf 50%,rgba(240,240,240,0) 100%)}
.cta-title{left:351px;top:836px;font-family:"Oswald",sans-serif;font-weight:500;font-size:14.5px;color:#2a2a2a}
.cta-text{left:351px;top:858px;font-size:8.5px;color:#333}
.cta-button{left:532px;top:880px;width:88px;height:21px;background:var(--purple-deep);color:var(--white);font-size:12px;display:flex;align-items:center;justify-content:center;border-right:3px solid #3b1e44;border-bottom:2px solid #3b1e44}

/* lower section */
.lower{left:0;top:931px;width:683px;height:216px;background:var(--grey-section);border-top:3px solid #d8d8d8}
.blog-title{left:46px;top:956px}
.post-photo{left:46px;top:1002px;width:89px;height:87px;background:linear-gradient(150deg,#e8c2aa,#c99479 60%,#8a5a48)}
.post-heading{left:144px;top:1000px;width:215px;font-family:"Arimo",Arial,sans-serif;font-weight:700;font-size:11px;line-height:13px;color:#111}
.post-meta{left:144px;top:1032px;font-size:7.5px;color:#333}
.post-meta span{margin-right:8px}
.post-excerpt{left:144px;top:1048px;width:210px;font-family:"Arimo",Arial,sans-serif;font-size:7.8px;line-height:10.5px;color:var(--muted)}
.post-rule{left:144px;top:1091px;width:206px;border-top:1px solid #cfcfcf}
.post-links{left:240px;top:1096px;font-size:7px;color:var(--purple-deep);display:flex;gap:10px;align-items:center}

.contact-title{left:422px;top:962px}
.contact-list{left:429px;top:1001px;font-size:7.6px;line-height:13.5px;color:#444}
.contact-row{display:flex;gap:4px}
.contact-row svg{flex:none;margin-top:3px}
.contact-row .indent{width:10px}
.social{left:429px;top:1096px;display:flex;gap:2px}
.social span{width:17px;height:17px;background:#c4c4c4}

/* footer */
.footer{left:0;top:1147px;width:683px;height:53px;background:var(--plum);border-top:3px solid var(--purple);color:var(--white);font-size:7px;text-align:center;padding-top:22px}
</style>
</head>
<body>

<div class="abs top-bar">
  <a class="item phone" href="tel:5552143860">
    <svg width="9" height="9" viewBox="0 0 10 10"><rect width="10" height="10" rx="1.5" fill="#444"/><path d="M3 2.2c.3-.2.6 0 .8.3l.5.9c.1.3 0 .5-.2.7l-.3.3c.3.7.9 1.3 1.6 1.6l.3-.3c.2-.2.5-.3.7-.2l.9.5c.3.2.4.5.3.8-.3.7-.9 1-1.6.8C4.9 7.2 2.9 5.2 2.6 3.8c-.1-.6.1-1.3.4-1.6z" fill="#fff"/></svg>
    (555) 214-3860
  </a>
  <a class="item mail" href="mailto:info@maplecovelaserdermalstudio.com">
    <svg width="11" height="8" viewBox="0 0 11 8"><rect width="11" height="8" rx="1" fill="#9a5bbd"/><path d="M.5 .8 5.5 4.6 10.5 .8" stroke="#fff" stroke-width="1" fill="none"/></svg>
    info@maplecovelaserdermalstudio.com
  </a>
</div>

<header>
  <a class="abs brand" href="http://maplecovelaserdermalstudio.com">
    <span class="brand-dot"></span>
    <span class="brand-name">Maple Cove Laser<br>Dermal Studio</span>
  </a>
  <nav class="abs main-nav">
    <a class="active" href="#">Home</a>
    <a href="#">About Us</a>
    <a href="#">Skin Renewal</a>
    <a href="#">Scar Removal</a>
    <a href="#">Wart Removal</a>
    <a href="#">Your Visit</a>
    <a href="#">Contact Us</a>
    <a href="#">Blog</a>
  </nav>
  <div class="abs header-rule"></div>
</header>

<section class="abs hero">
  <div class="hero-photo" role="img" aria-label="Photo of a smiling woman holding a pink lily to her cheek"></div>
</section>
<div class="abs hero-title">Maple Cove Laser Dermal Studio</div>
<div class="abs hero-tagline">LIVE BEAUTIFULLY</div>
<div class="abs hero-offer">Book a <strong>FREE</strong> Consultation Today!</div>
<a class="abs hero-phone" href="tel:5552143860">(555) 214-3860</a>
<div class="abs slider-dots"><span class="on"></span><span></span><span></span></div>

<section class="abs welcome">
  <h1>Welcome And Let Us Guide You in your Joureny to Rejuvenation!</h1>
  <p>Laser skin therapy is a non-invasive procedure that is extremely <mark>SAFE AND EFFECTIVE.</mark> Above all, it is discrete and you never have to worry about family, friends and acquaintances, finding out that you have had treatment for fine lines and wrinkles.<br>After each treatment, you will notice subtle but definite results. You will never have to hide indoors to wait for the skin irritation or bruising to disappear.<br>The treatment sessions are comfortable and there is no worry about using topical anesthetic gels.</p>
</section>

<h2 class="abs section-title faq-title">FAQ</h2>
<div class="abs faq">
  <div class="faq-item open">
    <div class="faq-head"><span class="faq-toggle">&minus;</span>How Does Laser Skin Renewal-Therapy Work?</div>
    <div class="faq-body">
      <p>When you have laser skin renewal session, your skin will be gently heated with the laser and this helps to stimulate production of collagen. The heating occurs in the upper dermal layer of your skin and this also dilates capillaries that help to reduce redness of your skin.</p>
      <p>Most people undergoing this treatment claim it is relaxing and soothing, without any discomfort or pain. Once your skin produces collagen, it will reduce the signs of wrinkles and fine lines.</p>
    </div>
  </div>
  <div class="faq-item" style="margin-top:9px"><div class="faq-head"><span class="faq-toggle">+</span>Are there any Side Effects of Laser Skin Renewal Therapy?</div></div>
  <div class="faq-item"><div class="faq-head"><span class="faq-toggle">+</span>Are laser skin treatments expensive?</div></div>
  <div class="faq-item"><div class="faq-head"><span class="faq-toggle">+</span>Number of Treatments?</div></div>
</div>

<h2 class="abs section-title results-title">Seeing is Believing</h2>
<a class="abs gallery-link" href="#"><svg width="5" height="6" viewBox="0 0 5 6"><path d="M0 0 5 3 0 6z" fill="#573657"/></svg>GALLERY</a>
<p class="abs results-text">Laser skin renewal does produce outstanding results. After mere five treatment sessions, you will notice a youthful glow about your skin and you also will find your skin looking smooth with an even tone.</p>

<div class="abs shot before" style="left:355px;top:633px"><div class="photo tone-a" role="img" aria-label="Before treatment: wrinkled facial skin"></div><div class="label">Before</div></div>
<div class="abs shot after" style="left:425px;top:633px"><div class="photo tone-b" role="img" aria-label="After treatment: smoother facial skin"></div><div class="label">After</div></div>
<div class="abs shot before" style="left:507px;top:633px"><div class="photo tone-c" role="img" aria-label="Before treatment: uneven skin tone"></div><div class="label">Before</div></div>
<div class="abs shot after" style="left:578px;top:633px"><div class="photo tone-d" role="img" aria-label="After treatment: even skin tone"></div><div class="label">After</div></div>
<div class="abs shot before" style="left:355px;top:729px"><div class="photo tone-e" role="img" aria-label="Before treatment: redness around the nose"></div><div class="label">Before</div></div>
<div class="abs shot after" style="left:425px;top:729px"><div class="photo tone-f" role="img" aria-label="After treatment: reduced redness"></div><div class="label">After</div></div>
<div class="abs shot before" style="left:507px;top:729px"><div class="photo tone-g" role="img" aria-label="Before treatment: scar near the lips"></div><div class="label">Before</div></div>
<div class="abs shot after" style="left:578px;top:729px"><div class="photo tone-h" role="img" aria-label="After treatment: faded scar"></div><div class="label">After</div></div>

<section class="abs cta">
  <div class="cta-photo" role="img" aria-label="Black and white close-up portrait of a woman"></div>
</section>
<div class="abs cta-title">Have more questions about laser skin treatments?</div>
<div class="abs cta-text">Our professionally trained staff is standing by to assist you...</div>
<a class="abs cta-button" href="#">Contact us</a>

<section class="abs lower"></section>
<h2 class="abs section-title blog-title">Recent Blog Post</h2>
<div class="abs post-photo" role="img" aria-label="Photo of a smiling woman resting her face on her hands"></div>
<h3 class="abs post-heading">Lorem ipsum dolor sit amet, consectetur adipiscing elit</h3>
<div class="abs post-meta"><span>Posted in: Dummy</span><span>Posted on: 13-11-2014</span></div>
<p class="abs post-excerpt">Lorem ipsum dolor sit amet, consectetur adipiscing elit. Suspendisse a odio luctus, blandit dui quis, tempor purus. Ut risus ligula, pulvinar ut vestibulum in, semper a velit.</p>
<div class="abs post-rule"></div>
<div class="abs post-links">
  <a href="#">2 comments <svg width="8" height="7" viewBox="0 0 8 7"><path d="M1 0h6a1 1 0 0 1 1 1v3a1 1 0 0 1-1 1H3L1 7V5a1 1 0 0 1-1-1V1a1 1 0 0 1 1-1z" fill="#7b3b91"/></svg></a>
  <span>|</span>
  <a href="#">Read more</a>
</div>

<h2 class="abs section-title contact-title">Contact info</h2>
<address class="abs contact-list" style="font-style:normal">
  <div class="contact-row">
    <svg width="8" height="10" viewBox="0 0 8 10"><path d="M4 0a4 4 0 0 1 4 4c0 2.6-4 6-4 6S0 6.6 0 4a4 4 0 0 1 4-4z" fill="#9a5bbd"/><circle cx="4" cy="4" r="1.4" fill="#ebebeb"/></svg>
    <div>Maple Cove Laser Dermal Studio<br>Harbor Medical Pavilion<br>2240 Cove Road, Suite 210<br>Maple Cove, TX 77590</div>
  </div>
  <div class="contact-row">
    <svg width="9" height="9" viewBox="0 0 10 10"><rect width="10" height="10" rx="1.5" fill="#7b3b91"/><path d="M3 2.2c.3-.2.6 0 .8.3l.5.9c.1.3 0 .5-.2.7l-.3.3c.3.7.9 1.3 1.6 1.6l.3-.3c.2-.2.5-.3.7-.2l.9.5c.3.2.4.5.3.8-.3.7-.9 1-1.6.8C4.9 7.2 2.9 5.2 2.6 3.8c-.1-.6.1-1.3.4-1.6z" fill="#fff"/></svg>
    <a href="tel:5552143860">(555) 214-3860</a>
  </div>
  <div class="contact-row">
    <svg width="9" height="7" viewBox="0 0 11 8"><rect width="11" height="8" rx="1" fill="#7b3b91"/><path d="M.5 .8 5.5 4.6 10.5 .8" stroke="#fff" stroke-width="1" fill="none"/></svg>
    <a href="mailto:info@maplecovelaserdermalstudio.com">info@maplecovelaserdermalstudio.com</a>
  </div>
</address>
<div class="abs social"><span></span><span></span><span></span></div>

<footer class="abs footer">Copyright 2015 maplecovelaserdermalstudio.com All Rights Reserved.</footer>

</body>
</html>
```